Brelto Kemp Flyer Insert

Hi my name is Dorian 

I’ve started a small company supplying hair brushes i need a small flyer made (most like will be A3 size or A4) that i aim to put in the packaging with my products … ive had a look at your portfolio and im a big fan of your work and feel you’d be the perfect designer to create what im looking for. the flyer needs to be a simple manual on how to achieve a hair pattern called 360 waves using my product. Ive had artwork created to go with the flyer and ive written instructions to go with each process of the art work. 

in terms of colour schemes i would like a cool modern black colour scheme theme … weather that is black and white or black and grey or black white and a variety of greys. i trust in your creativity to pull something really cool and professional off. let me know if this is something you be willing to work on and we can get straight down to the payments.

How To Properly Achieve 360 Waves 1. The most time efficient way to achieve waves  covering your entire head , is to start with a low and evenly cut hair cut.  2. Brush  your hair in a direction that your hair naturally grows ….  If you are unsure, brush where your hair best flattens and creates a swirl …from the swirl, brush outward towards the edge of your hair.  TIP: Brush your hair using long straight strokes as keeping a straight stroke creates a more uniform wave pattern. 3. Brush each section multiple times. The more consistent you brush , the more trained and uniform your waves become.  Fact: The Brelto Kemp Wave Brush is designed to cover more head space while brushing so it does not take as long as other regular brushes to achieve waves  Tip: Use a good pomade to help lock in your wave pattern progress in place.  Tip: Let the brush bristles do the work. DO NOT  press too hard, but allow brush bristles to gently pull and snap the hair into place using long straight strokes. 4. Tie hair down using a Durag or a stocking cap. Wear over night for best results.     REPEAT STEPS 1-4 Giving Your Self 3-4 Weeks Between Fresh Cuts  5  After Consistent Brushing , 360 Waves Should Be Complete After Several Months But Will Be Visible After A Couple Of Weeks … Remember Patients And consistency is key and #KEEPUPTHECOMBING #BreltoKemp

Requirements
Must have
• How To Properly Achieve 360 Waves
• 1.
• The most time efficient way to achieve waves  covering your entire head , is to start with a low and evenly cut hair cut. 
• 2.
• Brush  your hair in a direction that your hair naturally grows ….  If you are unsure, brush where your hair best flattens and creates a swirl …from the swirl, brush outward towards the edge of your hair. 
• TIP: Brush your hair using long straight strokes as keeping a straight stroke creates a more uniform wave pattern.
• 3. Brush each section multiple times. The more consistent you brush , the more trained and uniform your waves become. 
• Fact: The Brelto Kemp Wave Brush is designed to cover more head space while brushing so it does not take as long as other regular brushes to achieve waves 
• Tip: Use a good pomade to help lock in your wave pattern progress in place. 
• Tip: Let the brush bristles do the work. DO NOT  press too hard, but allow brush bristles to gently pull and snap the hair into place using long straight strokes.
• 4.
• Tie hair down using a Durag or a stocking cap. Wear over night for best results. 
•   
• REPEAT STEPS 1-4 Giving Your Self 3-4 Weeks Between Fresh Cuts 
• After Consistent Brushing , 360 Waves Should Be Complete After Several Months But Will Be Visible After A Couple Of Weeks … Remember Patients And consistency is key and #KEEPUPTHECOMBING #BreltoKemp

```html
<!DOCTYPE html>
<html lang="en">
<head>
<meta charset="utf-8">
<title>Brelto Kemp – How To Properly Achieve 360 Waves</title>
<link rel="stylesheet" href="https://fonts.googleapis.com/css2?family=Caprasimo&family=Arimo:wght@400&family=Lato:wght@400;700&display=swap">
<style>
  :root {
    --ink: #0c0c0c;
    --panel: #2e2e2e;
    --paper: #ffffff;
    --text-light: #f2f2f2;
    --figure: #5c6660;
    --stage: #e9e7e4;
  }
  * { margin: 0; padding: 0; box-sizing: border-box; }
  html, body { width: 1200px; height: 1200px; overflow: hidden; background: var(--stage); }
  .flyer {
    position: absolute; left: 186px; top: 20px;
    width: 983px; height: 1378px;
    transform: scale(0.8418); transform-origin: top left;
    background: var(--paper); overflow: hidden;
    font-family: "Lato", sans-serif; color: var(--text-light);
  }
  .flyer-shapes { position: absolute; inset: 0; }
  .brand {
    position: absolute; left: 770px; top: 40px; width: 160px;
    display: flex; flex-direction: column; align-items: center; gap: 14px;
  }
  .brand-dot { width: 64px; height: 64px; border-radius: 50%; background: var(--paper); }
  .brand-name {
    font-family: "Lato", sans-serif; font-weight: 700; font-size: 22px;
    letter-spacing: 2px; color: var(--paper); text-transform: uppercase; white-space: nowrap;
  }
  .title {
    position: absolute; left: 156px; top: 248px;
    font-family: "Caprasimo", serif; font-weight: 400; font-size: 74px; line-height: 78px;
    color: var(--paper);
  }
  .slogan {
    position: absolute; left: 701px; top: 560px; width: 275px;
    font-family: "Arimo", sans-serif; font-size: 21px; line-height: 27px; color: var(--ink);
  }
  .slogan .tag-brand { font-size: 26px; line-height: 34px; }
  .figure { position: absolute; background: linear-gradient(180deg, #3d3d3d, var(--figure)); border-radius: 40px 40px 6px 6px; }
  .step, .note { position: absolute; left: 94px; width: 860px; font-size: 15.5px; line-height: 19px; }
  .step { padding-left: 22px; }
  .step-num {
    position: absolute; left: 0; top: 0; width: 19px; height: 19px; border-radius: 50%;
    background: var(--paper); color: var(--ink); font-size: 13px; line-height: 19px; text-align: center;
  }
  .note b { font-weight: 700; }
  .fact { font-weight: 700; }
  .repeat { left: 101px; }
  .bulb { position: absolute; width: 26px; height: 26px; }
  .site {
    position: absolute; left: 0; right: 0; top: 1314px; text-align: center;
    font-size: 21px; letter-spacing: 0.5px; color: var(--paper);
  }
</style>
</head>
<body>
<main class="flyer">
  <svg class="flyer-shapes" viewBox="0 0 983 1378" width="983" height="1378" aria-hidden="true">
    <defs>
      <radialGradient id="photoTone" cx="0.45" cy="0.45" r="0.75">
        <stop offset="0" stop-color="#333333"/>
        <stop offset="0.7" stop-color="#262626"/>
        <stop offset="1" stop-color="#4a3a2c"/>
      </radialGradient>
    </defs>
    <path d="M0,690 C300,640 700,650 983,830 V1378 H0 Z" fill="var(--panel)"/>
    <path d="M0,1258 C260,1215 650,1225 983,1195 V1378 H0 Z" fill="var(--ink)"/>
  </svg>

  <svg class="flyer-shapes" viewBox="0 0 983 1378" width="983" height="1378" role="img" aria-label="Top-down photo of barber tools on a dark surface: round brushes, scissors, combs and pomade tins in bronze tones">
    <path d="M0,0 H983 V313 C840,400 480,600 0,640 Z" fill="url(#photoTone)"/>
  </svg>

  <svg class="flyer-shapes" viewBox="0 0 983 1378" width="983" height="1378" aria-hidden="true">
    <path d="M0,640 C480,600 840,400 983,313 V434 C860,500 500,650 0,665 Z" fill="var(--ink)"/>
    <path d="M430,0 C620,170 850,228 983,248 V0 Z" fill="var(--paper)"/>
    <path d="M495,0 C660,135 850,198 983,212 V0 Z" fill="var(--ink)"/>
    <path d="M455,0 C630,150 830,210 983,230" fill="none" stroke="var(--ink)" stroke-width="4"/>
  </svg>

  <div class="brand">
    <span class="brand-dot"></span>
    <span class="brand-name">Brelto Kemp</span>
  </div>

  <h1 class="title">How To Properly<br>Achieve 360 Waves</h1>

  <p class="slogan">Remember PATIENTS &amp; CONSISTENCY is key &amp; #KEEPUPTHECOMBING<br><span class="tag-brand">#BreltoKemp</span></p>

  <div class="figure" style="left:36px;top:722px;width:58px;height:78px" role="img" aria-label="Drawing of a man with a fresh low haircut"></div>
  <div class="figure" style="left:20px;top:802px;width:70px;height:66px" role="img" aria-label="Drawing of a man brushing his hair"></div>
  <div class="figure" style="left:14px;top:928px;width:76px;height:62px" role="img" aria-label="Drawing of a man brushing the side of his head"></div>
  <div class="figure" style="left:34px;top:1106px;width:56px;height:84px" role="img" aria-label="Drawing of a man wearing a durag"></div>
  <div class="figure" style="left:20px;top:1196px;width:70px;height:58px" role="img" aria-label="Drawing of a man showing finished 360 waves"></div>

  <p class="step" style="top:747px"><span class="step-num">1.</span>The most time efficient way to achieve waves &nbsp;covering your entire head , is to start with a low and<br>&nbsp;evenly cut hair cut</p>

  <p class="step" style="top:823px"><span class="step-num">2.</span>Brush &nbsp;your hair in a direction that your hair naturally grows .... &nbsp;If you are unsure, brush where your hair best flattens<br>and creates a swirl ...from the swirl, brush outward towards the edge of your hair.</p>

  <svg class="bulb" style="left:50px;top:882px" viewBox="0 0 26 26" aria-hidden="true"><g fill="none" stroke="#fff" stroke-width="1.6"><path d="M13 1v3M3 5l2 2M23 5l-2 2M1 13h3M25 13h-3"/></g><circle cx="13" cy="13" r="6" fill="#fff"/><rect x="10" y="19" width="6" height="4" fill="#fff"/></svg>
  <p class="note" style="top:893px"><b>TIP</b> : Brush your hair using long straight strokes as keeping a straight stroke creates a more uniform wave pattern</p>

  <p class="step" style="top:941px"><span class="step-num">3.</span>Brush each section multiple times. The more consistent you brush , the more trained and uniform your waves become.</p>
  <p class="note fact" style="top:975px">Fact: The Brelto Kemp Wave Brush is designed to cover more head space while brushing so it does not take as long<br>as other regular brushes to achieve waves</p>

  <svg class="bulb" style="left:47px;top:1020px" viewBox="0 0 26 26" aria-hidden="true"><g fill="none" stroke="#fff" stroke-width="1.6"><path d="M13 1v3M3 5l2 2M23 5l-2 2M1 13h3M25 13h-3"/></g><circle cx="13" cy="13" r="6" fill="#fff"/><rect x="10" y="19" width="6" height="4" fill="#fff"/></svg>
  <p class="note" style="top:1031px;left:90px"><b>Tip :</b> Use a good pomade to help lock in your wave pattern progress in place.</p>

  <svg class="bulb" style="left:47px;top:1053px" viewBox="0 0 26 26" aria-hidden="true"><g fill="none" stroke="#fff" stroke-width="1.6"><path d="M13 1v3M3 5l2 2M23 5l-2 2M1 13h3M25 13h-3"/></g><circle cx="13" cy="13" r="6" fill="#fff"/><rect x="10" y="19" width="6" height="4" fill="#fff"/></svg>
  <p class="note" style="top:1063px;left:90px"><b>Tip :</b> Let the brush bristles do the work. DO NOT &nbsp;press too hard, but allow brush bristles to gently pull and snap the hair<br>&nbsp;&nbsp;&nbsp;&nbsp;&nbsp;&nbsp;into place using long straight strokes.</p>

  <p class="step" style="top:1130px"><span class="step-num">4.</span>Tie hair down using a Durag or a stocking cap. Wear over night for best results.</p>
  <p class="note repeat" style="top:1173px">REPEAT STEPS 1-4 Giving Your Self 3-4 Weeks Between Fresh Cuts</p>

  <p class="step" style="top:1224px"><span class="step-num">5.</span>After Consistent Brushing , 360 Waves Should Be Complete After Several Months But Will Be Visible After A Couple<br>Of &nbsp;Weeks</p>

  <p class="site">www.wavebrushco.com</p>
</main>
</body>
</html>
```